Main Banner for Hullwrap.com, SIMPLE REDESIGN

We need to redesign the main banner that appears on the homepage of our website.

Attached in the project brief is a reference.

There are alot of things we like that we want to keep from that concept but its overall just something I drew on paint and not designed well.

1. Keep yellow tabs on the right hand side, we want them bigger and bolder and to showcase the bullet points inside.
2. Get rid of the 10 yr warranty emblem and replace that with our Brandell logo also attached to the brief.
3. Keep the bottom header and include hullwrap.com and the phone number, but make it look bolder and nicer.
4. Keep the watermark

Aside from these points what we really need is this but a better cleaner more professional version of it.

Target Market(s)

Visitors to our website hullwrap.com we want this banner to include all the major selling points, branding of the product and info on how to contact us.

Requirements
Must have
• Must be clean and professional. My fear is getting submissions that are too busy or messy. There are a lot of components but the challenge is to put them all in there in a clean professional way.
Should not have
• An image in the background like a beach or some kind of picture want the focus to be the requirements listed in the project description

```html
<!DOCTYPE html>
<html lang="en">
<head>
<meta charset="UTF-8">
<title>Brandell Supreme Boat Cover – Hullwrap.com</title>
<link href="https://fonts.googleapis.com/css2?family=Oswald:wght@400;500;600&display=swap" rel="stylesheet">
<style>
  :root {
    --yellow: #f6c21c;
    --white: #ffffff;
    --title-grey: #6b6b6b;
    --boat-light: #eceef0;
    --boat-mid: #c9ccd0;
    --boat-dark: #a6a9ad;
    --brand-dark: #3a3a3a;
  }
  * { margin: 0; padding: 0; box-sizing: border-box; }
  html, body { width: 1200px; height: 550px; overflow: hidden; background: var(--white); }
  .banner {
    position: relative;
    width: 1200px;
    height: 550px;
    background: var(--white);
    font-family: "Oswald", "Arial Narrow", sans-serif;
    overflow: hidden;
  }
  .brand-mark {
    position: absolute;
    left: 52px;
    top: 70px;
    display: flex;
    align-items: center;
    gap: 8px;
    color: var(--brand-dark);
    font-weight: 500;
    font-size: 26px;
    letter-spacing: 0.5px;
  }
  .brand-mark .dot {
    width: 14px;
    height: 14px;
    background: var(--yellow);
  }
  .headline {
    position: absolute;
    left: 198px;
    top: 30px;
    color: var(--title-grey);
    font-weight: 500;
    font-size: 60px;
    line-height: 1.2;
    letter-spacing: 1px;
    text-transform: uppercase;
  }
  .product-visual {
    position: absolute;
    left: 24px;
    top: 125px;
    width: 870px;
    height: 350px;
    background: radial-gradient(ellipse at 45% 45%, var(--boat-light) 0%, var(--boat-mid) 55%, rgba(255,255,255,0) 72%);
  }
  .features { list-style: none; }
  .feature-tab {
    position: absolute;
    right: 0;
    height: 57px;
    background: var(--yellow);
    color: var(--white);
    font-weight: 500;
    font-size: 32px;
    letter-spacing: 0.5px;
    text-transform: uppercase;
    display: flex;
    align-items: center;
    padding-left: 22px;
  }
  .feature-tab::before {
    content: "";
    width: 13px;
    height: 13px;
    border-radius: 50%;
    background: var(--white);
    margin-right: 18px;
  }
  .feature-tab.warranty { left: 864px; top: 139px; }
  .feature-tab.shipping { left: 896px; top: 222px; }
  .feature-tab.waterproof { left: 935px; top: 302px; }
  .contact-bar {
    position: absolute;
    left: 0;
    bottom: 0;
    width: 1200px;
    height: 70px;
    background: var(--yellow);
    color: var(--white);
    display: flex;
    align-items: center;
    text-transform: uppercase;
    font-weight: 500;
  }
  .contact-bar .site {
    position: absolute;
    left: 58px;
    font-size: 38px;
    letter-spacing: 1px;
  }
  .contact-bar .call {
    position: absolute;
    left: 588px;
    font-size: 36px;
    font-weight: 400;
    letter-spacing: 0.5px;
  }
  .contact-bar .call .number {
    font-size: 42px;
    font-weight: 500;
    margin-left: 6px;
  }
</style>
</head>
<body>
  <main class="banner">
    <div class="brand-mark"><span class="dot"></span>Brandell</div>
    <h1 class="headline">Brandell Supreme Boat Cover</h1>

    <div class="product-visual" role="img" aria-label="Boat fitted with a grey strapped cover, sitting on a twin-axle trailer"></div>

    <ul class="features">
      <li class="feature-tab warranty">10 Yr Warranty</li>
      <li class="feature-tab shipping">Free Shipping</li>
      <li class="feature-tab waterproof">Waterproof</li>
    </ul>

    <footer class="contact-bar">
      <span class="site">Hullwrap.com</span>
      <span class="call">Call us at:<span class="number">(800) 555-0142</span></span>
    </footer>
  </main>
</body>
</html>
```